Dunwick Consulting Powerpoint Template

I require a powerpoint template that I can use for presentations and for report writing. Template should include:
* Cover page with company logo and space for presentation title, and client logo if required.
* Proposed font and heading styles to match the logo (demonstrated through some sample text)
* Three different examples of presentation pages that can be tailored to different clients
* End page for contact details of the presenter or other report details. (so template should be five pages in total length)

The overall style of the template is professional, but with an eye-catching style.

Target Market(s)

Government clients

Industry/Entity Type

Government

Requirements
Must have
• Three different presentation pages that can be optional.
• Proposed font / heading styles for presentation with sample texts
• Use colour pallet: http://www.huetrellis.net/palette/417096/Velvet_Harbor
• Clear, crisp and professional design.
Should not have
• Pictures

```html
<!DOCTYPE html>
<html lang="en">
<head>
<meta charset="utf-8">
<title>Dunwick Consulting – Presentation Template</title>
<link href="https://fonts.googleapis.com/css2?family=Raleway:wght@300;400;500&display=swap" rel="stylesheet">
<style>
:root{
  --navy:#232b45;
  --tan:#d4b196;
  --sage:#9aa59d;
  --char:#3a3a3c;
  --ink:#55595f;
  --muted:#a4a6aa;
  --page:#ededed;
  --white:#ffffff;
}
*{margin:0;padding:0;box-sizing:border-box}
html,body{width:911px;height:1200px;overflow:hidden;background:var(--page)}
body{font-family:"Raleway",Arial,sans-serif;color:var(--ink)}
.canvas{position:relative;width:911px;height:1200px;overflow:hidden;background:var(--page)}
.slide{position:absolute;width:294px;height:165px;background:var(--white);overflow:hidden}
.c1{left:5px}.c2{left:308px}.c3{left:612px}
.r1{top:3px}.r2{top:173px}.r3{top:343px}.r4{top:513px}.r5{top:683px}.r6{top:853px}.r7{top:1023px}
.abs{position:absolute}
svg.bg{position:absolute;left:0;top:0}

/* brand */
.brand{position:absolute;text-align:center;color:var(--navy)}
.brand .dot{display:block;margin:0 auto 3px;border-radius:50%;background:var(--tan)}
.brand .name{display:block;font-weight:400;letter-spacing:3px;white-space:nowrap}
.brand-lg .dot{width:26px;height:26px}
.brand-lg .name{font-size:15px;letter-spacing:5px}
.brand-md .dot{width:13px;height:13px}
.brand-md .name{font-size:7.5px}
.brand-sm .dot{width:6px;height:6px;margin-bottom:1px}
.brand-sm .name{font-size:4px;letter-spacing:1.4px}

.partner{position:absolute;text-align:center;color:var(--muted);font-size:6.5px;white-space:nowrap}
.partner .ring{display:block;margin:0 auto 2px;width:16px;height:16px;border:1.2px solid var(--muted);border-radius:50%}
.partner-sm{font-size:3.6px}
.partner-sm .ring{width:8px;height:8px;border-width:.8px;margin-bottom:1px}
.divider-v{position:absolute;width:1px;height:26px;background:#d9d9d9}

.title{position:absolute;font-weight:300;letter-spacing:.3px;white-space:nowrap;text-transform:uppercase}
.t-lg{font-size:16.5px}
.t-md{font-size:12.5px}
.sub{position:absolute;font-size:5.5px;white-space:nowrap}
.navy-t{color:var(--navy)}
.white-t{color:var(--white)}
.right{text-align:right}
.center{text-align:center}

.band{position:absolute;height:20px}
.rule{position:absolute;left:0;width:294px;height:2px}

.footer{position:absolute;left:6px;right:6px;bottom:4px;height:12px;font-size:3px;color:var(--muted)}
.footer .brand{left:0;bottom:0}
.footer .copy{position:absolute;left:48px;bottom:3px}
.footer .num{position:absolute;right:44px;bottom:3px;color:var(--navy)}
.footer .partner{right:0;bottom:0}

.small{font-size:3.5px;line-height:1.4;color:var(--muted)}

/* agenda */
.agenda{position:absolute;display:flex;align-items:flex-start;gap:6px}
.agenda .time{width:24px;height:8px;background:var(--navy);color:var(--white);font-size:3.6px;line-height:8px;padding-left:2px}
.agenda h4{font-size:5.5px;font-weight:400;color:var(--ink)}
.agenda p{width:80px}

/* columns */
.col{position:absolute;top:0;height:100%;padding:0 5px;text-align:center}
.col .icon{display:block;margin:0 auto 6px;width:14px;height:14px;border:1px solid rgba(255,255,255,.85);border-radius:50%}
.col h4{font-size:5.5px;font-weight:400;color:rgba(255,255,255,.9);margin-bottom:2px}
.col p{font-size:3.3px;line-height:1.4;color:rgba(255,255,255,.85);text-align:justify}

.bullet{position:absolute;display:flex;gap:4px;width:62px}
.bullet .ic{flex:none;width:10px;height:10px;border-radius:50%}
.bullet h5{font-size:5px;font-weight:400}
.bullet p{font-size:2.8px;line-height:1.4;color:var(--muted)}

.tag{position:absolute;width:22px;height:9px;font-size:3px;color:var(--white);text-align:center;line-height:1.3;padding-top:1px}
.line{position:absolute;height:.8px;background:var(--navy)}
</style>
</head>
<body>
<div class="canvas">

<!-- 1 cover -->
<section class="slide c1 r1">
  <div class="brand brand-lg" style="left:0;right:0;top:55px"><span class="dot"></span><span class="name">DUNWICK</span><span class="name" style="font-size:6px;letter-spacing:3px">CONSULTING</span></div>
</section>

<!-- 2 navy cover -->
<section class="slide c2 r1" style="background:var(--navy)">
  <svg class="bg" width="294" height="165"><circle cx="64" cy="112" r="64" fill="var(--sage)"/><circle cx="64" cy="112" r="64" fill="none" stroke="var(--white)" stroke-width="3"/></svg>
  <div class="title t-lg white-t right" style="right:11px;top:28px">Your Title Goes Here</div>
  <div class="sub white-t right" style="right:11px;top:48px">Your Subtitle Goes Here</div>
  <div class="sub white-t right" style="right:11px;top:141px">Mara Quill</div>
</section>

<!-- 3 tan band -->
<section class="slide c3 r1">
  <div class="band" style="left:0;top:59px;width:100px;background:var(--tan);clip-path:polygon(0 0,100% 0,86% 100%,0 100%)"></div>
  <div class="brand brand-md" style="left:170px;top:52px"><span class="dot"></span><span class="name">DUNWICK</span></div>
  <div class="divider-v" style="left:228px;top:56px"></div>
  <div class="partner" style="left:232px;top:56px"><span class="ring"></span>Northfold Labels</div>
  <div class="title t-lg navy-t right" style="right:11px;top:113px">Your Title Goes Here</div>
  <div class="sub navy-t right" style="right:11px;top:133px">Your Subtitle Goes Here</div>
</section>

<!-- 4 sage band -->
<section class="slide c1 r2">
  <div class="band" style="left:0;top:59px;width:103px;background:var(--sage);clip-path:polygon(0 0,100% 0,86% 100%,0 100%)"></div>
  <div class="brand brand-md" style="left:139px;top:52px"><span class="dot"></span><span class="name">DUNWICK</span></div>
  <div class="divider-v" style="left:200px;top:56px"></div>
  <div class="partner" style="left:230px;top:56px"><span class="ring"></span>Northfold Labels</div>
  <div class="title t-lg navy-t right" style="right:11px;top:113px">Your Title Goes Here</div>
  <div class="sub navy-t right" style="right:11px;top:133px">Your Subtitle Goes Here</div>
</section>

<!-- 5 navy band -->
<section class="slide c2 r2">
  <div class="band" style="left:0;top:59px;width:103px;background:var(--navy);clip-path:polygon(0 0,100% 0,86% 100%,0 100%)"></div>
  <div class="brand brand-md" style="left:139px;top:52px"><span class="dot"></span><span class="name">DUNWICK</span></div>
  <div class="divider-v" style="left:200px;top:56px"></div>
  <div class="partner" style="left:230px;top:56px"><span class="ring"></span>Northfold Labels</div>
  <div class="title t-lg navy-t right" style="right:11px;top:111px">Your Title Goes Here</div>
  <div class="sub navy-t right" style="right:11px;top:131px">Your Subtitle Goes Here</div>
</section>

<!-- 6 sage rule -->
<section class="slide c3 r2">
  <div class="brand brand-md" style="left:76px;top:54px"><span class="dot"></span><span class="name">DUNWICK</span></div>
  <div class="divider-v" style="left:138px;top:58px"></div>
  <div class="partner" style="left:166px;top:58px"><span class="ring"></span>Northfold Labels</div>
  <div class="rule" style="top:110px;background:var(--sage)"></div>
  <div class="title t-lg navy-t center" style="left:0;right:0;top:122px">Your Title Goes Here</div>
  <div class="sub navy-t center" style="left:0;right:0;top:142px">Your Subtitle Goes Here</div>
</section>

<!-- 7 tan rule -->
<section class="slide c1 r3">
  <div class="brand brand-md" style="left:76px;top:54px"><span class="dot"></span><span class="name">DUNWICK</span></div>
  <div class="divider-v" style="left:138px;top:58px"></div>
  <div class="partner" style="left:166px;top:58px"><span class="ring"></span>Northfold Labels</div>
  <div class="rule" style="top:110px;background:var(--tan)"></div>
  <div class="title t-lg navy-t center" style="left:0;right:0;top:122px">Your Title Goes Here</div>
  <div class="sub navy-t center" style="left:0;right:0;top:142px">Your Subtitle Goes Here</div>
</section>

<!-- 8 navy rule -->
<section class="slide c2 r3">
  <div class="brand brand-md" style="left:76px;top:54px"><span class="dot"></span><span class="name">DUNWICK</span></div>
  <div class="divider-v" style="left:138px;top:58px"></div>
  <div class="partner" style="left:166px;top:58px"><span class="ring"></span>Northfold Labels</div>
  <div class="rule" style="top:110px;background:var(--navy)"></div>
  <div class="title t-lg navy-t center" style="left:0;right:0;top:122px">Your Title Goes Here</div>
  <div class="sub navy-t center" style="left:0;right:0;top:142px">Your Subtitle Goes Here</div>
</section>

<!-- 9 tan diagonal -->
<section class="slide c3 r3">
  <svg class="bg" width="294" height="165"><polygon points="96,0 294,0 294,86 202,165 0,165 0,74" fill="var(--tan)"/><line x1="0" y1="74" x2="96" y2="0" stroke="var(--navy)" stroke-width=".6"/><line x1="202" y1="165" x2="294" y2="86" stroke="var(--navy)" stroke-width=".6"/></svg>
  <div class="brand brand-sm" style="left:8px;top:16px"><span class="dot"></span><span class="name">DUNWICK</span></div>
  <div class="title t-lg white-t right" style="right:16px;top:67px">Your Title Goes Here</div>
  <div class="sub white-t right" style="right:38px;top:88px">Your Subtitle Goes Here</div>
  <div class="partner partner-sm" style="right:8px;top:135px"><span class="ring"></span>Northfold Labels</div>
</section>

<!-- 10 sage diagonal -->
<section class="slide c1 r4">
  <svg class="bg" width="294" height="165"><polygon points="93,0 294,0 294,86 202,165 0,165 0,74" fill="var(--sage)"/><line x1="0" y1="74" x2="93" y2="0" stroke="var(--navy)" stroke-width=".6"/><line x1="202" y1="165" x2="294" y2="86" stroke="var(--tan)" stroke-width=".6"/></svg>
  <div class="brand brand-sm" style="left:8px;top:16px"><span class="dot"></span><span class="name">DUNWICK</span></div>
  <div class="title t-lg white-t right" style="right:38px;top:67px">Your Title Goes Here</div>
  <div class="sub white-t right" style="right:38px;top:88px">Your Subtitle Goes Here</div>
  <div class="partner partner-sm" style="right:12px;top:135px"><span class="ring"></span>Northfold Labels</div>
</section>

<!-- 11 navy diagonal -->
<section class="slide c2 r4">
  <svg class="bg" width="294" height="165"><polygon points="93,0 294,0 294,86 202,165 0,165 0,74" fill="var(--navy)"/><line x1="202" y1="165" x2="294" y2="86" stroke="var(--tan)" stroke-width=".6"/></svg>
  <div class="brand brand-sm" style="left:8px;top:16px"><span class="dot"></span><span class="name">DUNWICK</span></div>
  <div class="title t-lg white-t right" style="right:38px;top:67px">Your Title Goes Here</div>
  <div class="sub white-t right" style="right:38px;top:88px">Your Subtitle Goes Here</div>
  <div class="partner partner-sm" style="right:12px;top:135px"><span class="ring"></span>Northfold Labels</div>
</section>

<!-- 12 agenda -->
<section class="slide c3 r4">
  <div class="title t-md navy-t" style="left:15px;top:12px">Our Agenda</div>
  <div class="rule" style="top:30px;height:.6px;background:#e2e2e2"></div>
  <div class="agenda" style="left:26px;top:46px"><div class="time">10:00 ⏱</div><div><h4>Agenda One</h4><p class="small">Short note on the opening topic and aims.</p></div></div>
  <div class="agenda" style="left:26px;top:80px"><div class="time">11:00 ⏱</div><div><h4>Agenda Two</h4><p class="small">Short note on the second topic and aims.</p></div></div>
  <div class="agenda" style="left:26px;top:116px"><div class="time">12:00 ⏱</div><div><h4>Agenda Three</h4><p class="small">Short note on the third topic and aims.</p></div></div>
  <div class="agenda" style="left:149px;top:46px"><div class="time">13:00 ⏱</div><div><h4>Agenda Four</h4><p class="small">Short note on the fourth topic and aims.</p></div></div>
  <div class="agenda" style="left:149px;top:80px"><div class="time">14:00 ⏱</div><div><h4>Agenda Five</h4><p class="small">Short note on the fifth topic and aims.</p></div></div>
  <div class="agenda" style="left:149px;top:116px"><div class="time">15:00 ⏱</div><div><h4>Agenda Six</h4><p class="small">Short note on the closing topic and aims.</p></div></div>
  <div class="footer"><div class="brand brand-sm"><span class="dot"></span><span class="name">DUNWICK</span></div><span class="copy">© 2017 DUNWICK CONSULTING. All rights reserved.</span><span class="num">11</span><div class="partner partner-sm"><span class="ring"></span>Northfold Labels</div></div>
</section>

<!-- 13 four columns -->
<section class="slide c1 r5">
  <div class="title t-md navy-t" style="left:14px;top:12px">Your Title Here</div>
  <div class="abs" style="left:0;top:53px;width:294px;height:82px">
    <div class="col" style="left:0;width:74px;background:var(--tan);padding-top:12px"><span class="icon"></span><h4>Heading Here</h4><p>Plain summary text for this point, kept brief and clear for readers.</p></div>
    <div class="col" style="left:73px;width:74px;background:var(--sage);padding-top:12px"><span class="icon"></span><h4>Heading Here</h4><p>Plain summary text for this point, kept brief and clear for readers.</p></div>
    <div class="col" style="left:147px;width:74px;background:var(--navy);padding-top:12px"><span class="icon"></span><h4>Heading Here</h4><p>Plain summary text for this point, kept brief and clear for readers.</p></div>
    <div class="col" style="left:220px;width:74px;background:var(--char);padding-top:12px"><span class="icon"></span><h4>Heading Here</h4><p>Plain summary text for this point, kept brief and clear for readers.</p></div>
  </div>
  <div class="footer"><div class="brand brand-sm"><span class="dot"></span><span class="name">DUNWICK</span></div><span class="copy">© 2017 DUNWICK CONSULTING. All rights reserved.</span><span class="num">12</span><div class="partner partner-sm"><span class="ring"></span>Northfold Labels</div></div>
</section>

<!-- 14 divider page -->
<section class="slide c2 r5">
  <div class="brand brand-md" style="left:210px;top:58px"><span class="dot"></span><span class="name">DUNWICK</span></div>
  <div class="title t-md navy-t right" style="right:34px;top:96px">Divider Page</div>
  <div class="sub navy-t right" style="right:34px;top:111px">Subtitle Here</div>
  <p class="small right abs" style="right:34px;top:120px;width:105px">Short supporting text that introduces the next section of the report.</p>
</section>

<!-- 15 text & bullets -->
<section class="slide c3 r5">
  <div class="title t-md navy-t" style="left:14px;top:12px">Text &amp; Bullet Area</div>
  <div class="abs" style="left:16px;top:52px;font-size:5px">Heading Goes Here</div>
  <p class="small abs" style="left:16px;top:62px;width:80px">Opening paragraph that sets out the main message in plain terms for the reader.<br><br>Second paragraph with added detail and a brief note on scope.<br><br>Closing line that sums up the key point.</p>
  <div class="bullet" style="left:114px;top:50px"><span class="ic" style="background:var(--tan)"></span><div><h5 style="color:var(--tan)">Your Text Here</h5><p>Brief note on this item.</p></div></div>
  <div class="bullet" style="left:114px;top:74px"><span class="ic" style="background:var(--sage)"></span><div><h5 style="color:var(--sage)">Your Text Here</h5><p>Brief note on this item.</p></div></div>
  <div class="bullet" style="left:114px;top:98px"><span class="ic" style="background:var(--navy)"></span><div><h5 style="color:var(--navy)">Your Text Here</h5><p>Brief note on this item.</p></div></div>
  <div class="bullet" style="left:114px;top:122px"><span class="ic" style="background:var(--tan)"></span><div><h5 style="color:var(--tan)">Your Text Here</h5><p>Brief note on this item.</p></div></div>
  <div class="bullet" style="left:207px;top:50px"><span class="ic" style="background:var(--sage)"></span><div><h5 style="color:var(--sage)">Your Text Here</h5><p>Brief note on this item.</p></div></div>
  <div class="bullet" style="left:207px;top:74px"><span class="ic" style="background:var(--navy)"></span><div><h5 style="color:var(--navy)">Your Text Here</h5><p>Brief note on this item.</p></div></div>
  <div class="bullet" style="left:207px;top:98px"><span class="ic" style="background:var(--tan)"></span><div><h5 style="color:var(--tan)">Your Text Here</h5><p>Brief note on this item.</p></div></div>
  <div class="bullet" style="left:207px;top:122px"><span class="ic" style="background:var(--sage)"></span><div><h5 style="color:var(--sage)">Your Text Here</h5><p>Brief note on this item.</p></div></div>
  <div class="footer"><div class="brand brand-sm"><span class="dot"></span><span class="name">DUNWICK</span></div><span class="copy">© 2017 DUNWICK CONSULTING. All rights reserved.</span><span class="num">15</span><div class="partner partner-sm"><span class="ring"></span>Northfold Labels</div></div>
</section>

<!-- 16 five columns -->
<section class="slide c1 r6">
  <div class="col" style="left:0;width:59px;background:var(--tan);padding-top:40px"><span class="icon"></span><h4 style="margin-top:20px">Heading Here</h4><p>Plain text for this column, short and easy to scan.</p></div>
  <div class="col" style="left:59px;width:59px;background:var(--tan);border-left:.6px solid rgba(255,255,255,.5);padding-top:40px"><span class="icon"></span><h4 style="margin-top:20px">Heading Here</h4><p>Plain text for this column, short and easy to scan.</p></div>
  <div class="col" style="left:118px;width:59px;background:var(--tan);border-left:.6px solid rgba(255,255,255,.5);padding-top:40px"><span class="icon"></span><h4 style="margin-top:20px">Heading Here</h4><p>Plain text for this column, short and easy to scan.</p></div>
  <div class="col" style="left:177px;width:59px;background:var(--tan);border-left:.6px solid rgba(255,255,255,.5);padding-top:40px"><span class="icon"></span><h4 style="margin-top:20px">Heading Here</h4><p>Plain text for this column, short and easy to scan.</p></div>
  <div class="col" style="left:236px;width:58px;background:var(--sage);padding-top:40px"><span class="icon"></span><h4 style="margin-top:20px">Heading Here</h4><p>Plain text for this column, short and easy to scan.</p></div>
</section>

<!-- 17 mockup area -->
<section class="slide c2 r6">
  <div class="title t-md navy-t" style="left:14px;top:12px">Our Mockup Area</div>
  <div class="abs" style="left:0;top:95px;width:294px;height:70px;background:var(--navy)"></div>
  <div class="abs" style="left:230px;top:95px;width:64px;height:70px;background:#4a5168"></div>
  <div class="abs" role="img" aria-label="Laptop screen showing the Dunwick Consulting title slide" style="left:62px;top:30px;width:170px;height:112px;background:linear-gradient(180deg,#f4f4f4,#dcdcdc);border:3px solid #2b2b2b;border-radius:4px 4px 0 0"></div>
  <div class="abs" style="left:50px;top:142px;width:194px;height:5px;background:#bfbfbf;border-radius:0 0 4px 4px"></div>
  <div class="brand brand-md" style="left:112px;top:72px"><span class="dot"></span><span class="name">DUNWICK</span></div>
  <div class="tag" style="left:14px;top:55px;background:var(--navy)">Your Text Goes Here</div>
  <div class="tag" style="left:14px;top:79px;background:var(--sage)">Your Text Goes Here</div>
  <div class="tag" style="left:14px;top:110px;background:var(--tan)">Your Text Goes Here</div>
  <div class="tag" style="left:258px;top:55px;background:var(--tan)">Your Text Goes Here</div>
  <div class="tag" style="left:258px;top:79px;background:var(--navy)">Your Text Goes Here</div>
  <div class="tag" style="left:258px;top:110px;background:var(--sage)">Your Text Goes Here</div>
  <div class="line" style="left:36px;top:59px;width:90px"></div>
  <div class="line" style="left:36px;top:83px;width:48px;background:var(--sage)"></div>
  <div class="line" style="left:190px;top:59px;width:68px;background:var(--tan)"></div>
  <div class="line" style="left:200px;top:83px;width:58px"></div>
</section>

<!-- 18 right picture / chart -->
<section class="slide c3 r6">
  <div class="abs" style="left:0;top:0;width:145px;height:165px;background:var(--navy)"></div>
  <div class="abs" style="left:32px;top:28px;width:82px;height:82px;border:2px solid var(--white);border-radius:50%"></div>
  <div class="abs center" style="left:32px;top:48px;width:82px;color:var(--tan);font-size:12px;font-weight:300;line-height:1.25">RIGHT<br>PICTURE<br>SLIDE</div>
  <p class="abs center" style="left:30px;top:118px;width:86px;font-size:3.2px;line-height:1.4;color:var(--white)">A short caption line sits here<br>to explain the visual beside<br>and its main point.</p>
  <svg class="abs" style="left:172px;top:28px" width="110" height="70">
    <g fill="var(--tan)"><rect x="0" y="10" width="4" height="54"/><rect x="30" y="14" width="4" height="50"/><rect x="60" y="20" width="4" height="44"/><rect x="88" y="14" width="4" height="50"/></g>
    <g fill="var(--sage)"><rect x="6" y="40" width="4" height="24"/><rect x="36" y="24" width="4" height="40"/><rect x="66" y="30" width="4" height="34"/><rect x="94" y="4" width="4" height="60"/></g>
    <g fill="var(--navy)"><rect x="12" y="26" width="4" height="38"/><rect x="42" y="40" width="4" height="24"/><rect x="72" y="18" width="4" height="46"/><rect x="100" y="0" width="4" height="64"/></g>
    <line x1="0" y1="64.5" x2="106" y2="64.5" stroke="#ccc" stroke-width=".5"/>
  </svg>
  <div class="abs" style="left:160px;top:105px;font-size:17px;font-weight:300;color:var(--navy)"><span style="color:var(--tan);font-size:9px">▲</span>85%</div>
  <p class="abs" style="left:172px;top:124px;font-size:4px;color:var(--navy)">Profit</p>
  <p class="small abs" style="left:172px;top:131px;width:55px;font-size:3px">Brief note on the year result and its trend.</p>
</section>

<!-- 19 our mockup -->
<section class="slide c1 r7">
  <div class="title t-md navy-t" style="left:14px;top:12px">Our Mockup</div>
  <div class="abs" style="left:14px;top:38px;font-size:5.5px;color:var(--tan)">Heading Here</div>
  <p class="small abs" style="left:14px;top:46px;width:112px">Short paragraph on the display and what it shows, set out in two or three clear lines for the reader.</p>
  <div class="abs" style="left:0;top:72px;width:145px;height:93px;background:var(--page)"></div>
  <div class="bullet" style="left:14px;top:82px;width:110px"><span class="ic" style="background:var(--tan);width:8px;height:8px"></span><p>Brief point on the first feature with a short plain line of detail.</p></div>
  <div class="bullet" style="left:14px;top:104px;width:110px"><span class="ic" style="background:var(--sage);width:8px;height:8px"></span><p>Brief point on the second feature with a short plain line of detail.</p></div>
  <div class="abs" role="img" aria-label="Desktop monitor displaying the Dunwick Consulting title slide" style="left:130px;top:12px;width:160px;height:110px;background:linear-gradient(180deg,#fafafa,#e4e4e4);border:5px solid #1e1e1e;border-radius:4px"></div>
  <div class="abs" style="left:198px;top:122px;width:24px;height:12px;background:#cfcfcf"></div>
  <div class="brand brand-md" style="left:178px;top:52px"><span class="dot"></span><span class="name">DUNWICK</span></div>
  <div class="footer"><div class="brand brand-sm"><span class="dot"></span><span class="name">DUNWICK</span></div><span class="copy">© 2017 DUNWICK CONSULTING. All rights reserved.</span><span class="num">19</span><div class="partner partner-sm"><span class="ring"></span>Northfold Labels</div></div>
</section>

<!-- 20 line chart -->
<section class="slide c2 r7">
  <div class="title t-md navy-t" style="left:20px;top:32px;line-height:1.15">This is Line<br>Chart Slide</div>
  <div class="abs" style="left:20px;top:74px;width:66px;height:8px;background:var(--navy);color:var(--white);font-size:3.6px;line-height:8px;text-align:center">CREATIVE TEXT HERE</div>
  <p class="small abs" style="left:24px;top:90px;width:72px"><span style="color:var(--navy)">Lorem Ipsum</span> short text that explains the trend in the chart and its main turn points.</p>
  <svg class="abs" style="left:125px;top:34px" width="160" height="100" font-family="Raleway, sans-serif">
    <g font-size="3" fill="#aaa"><text x="0" y="4">5</text><text x="0" y="24">4</text><text x="0" y="44">3</text><text x="0" y="64">2</text><text x="0" y="84">1</text><text x="12" y="98">Category 1</text><text x="50" y="98">Category 2</text><text x="88" y="98">Category 3</text><text x="124" y="98">Category 4</text></g>
    <line x1="8" y1="90" x2="156" y2="90" stroke="#ddd" stroke-width=".4"/>
    <polyline points="18,20 56,62 94,48 132,28" fill="none" stroke="var(--sage)" stroke-width="1.3"/>
    <polyline points="18,52 56,28 94,76 132,66" fill="none" stroke="var(--tan)" stroke-width="1.3"/>
  </svg>
  <div class="footer"><div class="brand brand-sm"><span class="dot"></span><span class="name">DUNWICK</span></div><span class="copy">© 2017 DUNWICK CONSULTING. All rights reserved.</span><span class="num">20</span><div class="partner partner-sm"><span class="ring"></span>Northfold Labels</div></div>
</section>

<!-- 21 navy divider -->
<section class="slide c3 r7" style="background:var(--navy)">
  <svg class="bg" width="294" height="165"><polygon points="294,86 294,165 202,165" fill="var(--white)"/></svg>
  <div class="title t-lg white-t right" style="right:38px;top:69px">This is Your Divider Page</div>
  <div class="sub white-t right" style="right:38px;top:90px">Your Subtitle Goes Here</div>
  <div class="brand brand-sm" style="right:8px;top:144px"><span class="dot"></span><span class="name">DUNWICK</span></div>
</section>

</div>
</body>
</html>
```